Design of Product Brochure

TLM Survey Advisory, based in Namibia, is launching a premium charcoal brand: Embera Charcoal. We manufacture two distinct, high-quality product lines: one for the serious home barbecuer and one for professional restaurant kitchens.
The objective of this project is to create a cohesive and compelling visual identity across a product brochure (for B2B sales and high-end B2C) and a marketing website. The designs must elevate Embera Charcoal from a simple commodity to a premium, trusted fuel choice, emphasizing its Namibian origin, scientific backing, and superior performance.

```html
<!DOCTYPE html>
<html lang="en">
<head>
<meta charset="utf-8">
<title>Embera Charcoal – Tri-fold Brochure</title>
<link href="https://fonts.googleapis.com/css2?family=Montserrat:wght@400;500;600;700;800&display=swap" rel="stylesheet">
<style>
:root{
  --red:#c4161c;
  --black:#0c0c0c;
  --dark:#1d1d1d;
  --white:#ffffff;
  --ink:#1a1a1a;
  --bg:#e6e6e6;
  --ember:#e2561a;
  --kraft:#c9a06a;
}
*{margin:0;padding:0;box-sizing:border-box}
html,body{width:844px;height:1200px;overflow:hidden;background:var(--bg);font-family:'Montserrat',sans-serif}
.spread{position:absolute;left:39px;width:766px;height:541px;display:flex}
.spread--outside{top:43px}
.spread--inside{top:617px}
.panel{position:relative;width:255.33px;height:100%;overflow:hidden}
.panel--black{background:var(--black);color:var(--white)}
.panel--dark{background:var(--dark);color:var(--white)}
.panel--white{background:var(--white);color:var(--ink)}
.bar-top{position:absolute;top:0;left:0;right:0;height:2px;background:var(--red)}
.bar-bottom{position:absolute;bottom:0;left:0;right:0;height:3px;background:var(--red);z-index:3}
.photo{position:absolute}
.h-red{color:var(--red)}
.title{font-weight:800;font-size:15px;line-height:19px;text-transform:uppercase}
/* about */
.about{position:absolute;left:22px;top:29px;width:206px}
.about .tagline{margin-top:10px;font-weight:800;font-size:10px;line-height:14px}
.about p{margin-top:11px;font-size:7.6px;line-height:13.1px;text-align:justify;color:#eee}
/* cover middle */
.brand-mark{position:absolute;left:50%;top:232px;transform:translateX(-50%);width:104px;height:104px;border-radius:50%;background:var(--red)}
.cover-head{position:absolute;top:372px;left:0;right:0;text-align:center;font-weight:800;font-size:15px;line-height:20px}
.cover-sub{position:absolute;top:420px;left:30px;right:30px;text-align:center;font-size:8px;line-height:11px}
.contacts{position:absolute;top:458px;left:18px;right:10px;display:grid;grid-template-columns:1fr 1fr;row-gap:16px}
.contact{display:flex;gap:7px;align-items:flex-start}
.contact svg{flex:none;width:16px;height:16px}
.contact .lbl{font-size:6px;color:var(--red)}
.contact .val{font-size:6.4px;margin-top:1px}
/* cover right */
.logo{position:absolute;top:58px;left:0;right:0;text-align:center;font-weight:800;font-size:19px;color:var(--white);display:flex;justify-content:center;align-items:center;gap:7px}
.logo i{display:block;width:16px;height:16px;border-radius:50%;background:var(--red)}
.cover-title{position:absolute;top:109px;left:0;right:0;text-align:center;font-weight:800;font-size:19.5px;line-height:23.5px;z-index:2}
/* products */
.product{position:absolute;left:19px;width:220px}
.product .sub{margin-top:12px;font-weight:600;font-size:10.5px;line-height:14px}
.product p{margin-top:10px;font-size:8.3px;line-height:12.2px}
.bullets{list-style:none;margin-top:10px}
.bullets li{display:flex;align-items:center;gap:7px;font-size:6.8px;font-weight:600;margin-bottom:8.6px}
.bullets li::before{content:"";width:6px;height:6px;background:var(--red);border-radius:50%;flex:none}
/* science */
.science{position:absolute;left:27px;top:26px;right:20px}
.science .kicker{margin-top:9px;font-weight:700;font-size:6.3px}
.feature{position:absolute;left:24px;right:22px;height:80px}
.feature svg{position:absolute;left:0;top:0;width:34px;height:34px}
.feature .body{position:absolute;left:47px;right:0;top:0}
.feature h3{font-size:7.6px;font-weight:700}
.feature .rule{width:24px;height:1px;background:var(--red);margin:6px 0 9px}
.feature p{font-size:4.6px;line-height:7.8px;color:#ddd}
</style>
</head>
<body>

<!-- Outside spread -->
<section class="spread spread--outside">
  <div class="panel panel--black">
    <div class="about">
      <div class="title"><span class="h-red">About</span><br>Embera Charcoal</div>
      <div class="tagline">ROOTED IN NAMIBIA. BACKED BY SCIENCE. CRAFTED FOR PERFORMANCE.</div>
      <p>From the heart of Namibia’s dense hardwood forests, Embera Charcoal is produced with meticulous care and scientific precision. Developed by TLM Survey Advisory, our mission is simple: to transform charcoal from a common fuel into a trusted, premium-grade energy source.</p>
      <p style="margin-top:12px">Sustainably sourced, rigorously tested, and engineered for superior performance—Embera Charcoal stands apart. Sed ut perspiciatis unde omnis iste natus error sit voluptatem accusantium doloremque laudantium, totam rem aperiam, eaque ipsa quae ab illo inventore veritatis et quasi architecto beatae vitae dicta sunt explicabo.</p>
    </div>
    <div class="photo" role="img" aria-label="Photo of glowing charcoal embers with sparks" style="left:0;right:0;top:334px;bottom:0;background:radial-gradient(ellipse at 50% 45%,#f07a1e 0%,#b8340e 30%,#2a1a16 65%,#0c0c0c 100%)"></div>
    <div class="bar-bottom"></div>
  </div>

  <div class="panel panel--black" style="background:#181818">
    <div class="bar-top" style="z-index:2"></div>
    <div class="photo" role="img" aria-label="Close-up photo of charcoal chunks with red glow between them" style="left:0;right:0;top:0;height:185px;background:radial-gradient(ellipse at 50% 40%,#b3121a 0%,#4a0c0e 45%,#141414 80%,#181818 100%)"></div>
    <div class="brand-mark" aria-hidden="true"></div>
    <div class="cover-head">FUEL YOUR FIRE<br>WITH <span class="h-red">EMBERA CHARCOAL</span></div>
    <div class="cover-sub">Premium Namibian Charcoal. Backed by Science. Trusted Worldwide.</div>
    <div class="contacts">
      <div class="contact">
        <svg viewBox="0 0 16 16"><circle cx="8" cy="8" r="8" fill="#c4161c"/><rect x="4.3" y="5.3" width="7.4" height="5.4" rx=".6" fill="#fff"/><path d="M4.5 5.6 8 8.3l3.5-2.7" stroke="#c4161c" stroke-width=".8" fill="none"/></svg>
        <div><div class="lbl">Email</div><div class="val">sales@emberacharcoal.com</div></div>
      </div>
      <div class="contact">
        <svg viewBox="0 0 16 16"><circle cx="8" cy="8" r="8" fill="#c4161c"/><path d="M5.4 4.4c.4-.3.8-.2 1 .2l.7 1.3c.2.4 0 .7-.3 1l-.4.3c.4.9 1.1 1.6 2 2l.3-.4c.3-.3.6-.5 1-.3l1.3.7c.4.2.5.6.2 1-.6.9-1.4 1.2-2.4.8C7.100 10.3 5.700 8.9 5 7.1c-.4-1 0-2 .4-2.700z" fill="#fff"/></svg>
        <div><div class="lbl">Phone:</div><div class="val">+1 555 0142 7788</div></div>
      </div>
      <div class="contact">
        <svg viewBox="0 0 16 16"><circle cx="8" cy="8" r="8" fill="#c4161c"/><path d="M8 3.8a2.7 2.7 0 0 0-2.7 2.7C5.3 8.6 8 12 8 12s2.7-3.4 2.7-5.5A2.7 2.7 0 0 0 8 3.8z" fill="#fff"/><circle cx="8" cy="6.5" r="1" fill="#c4161c"/></svg>
        <div><div class="lbl">Address</div><div class="val">PO Box 48, Lorem Street</div></div>
      </div>
      <div class="contact">
        <svg viewBox="0 0 16 16"><circle cx="8" cy="8" r="8" fill="#c4161c"/><g fill="none" stroke="#fff" stroke-width=".8"><circle cx="8" cy="8" r="3.6"/><ellipse cx="8" cy="8" rx="1.5" ry="3.6"/><path d="M4.4 8h7.2"/></g></svg>
        <div><div class="lbl">Web</div><div class="val">www.emberacharcoal.com</div></div>
      </div>
    </div>
    <div class="bar-bottom"></div>
  </div>

  <div class="panel panel--black" style="background:#121212">
    <div class="photo" role="img" aria-label="Photo of a pile of charcoal chunks burning with tall orange flames" style="left:0;right:0;top:160px;bottom:0;background:radial-gradient(ellipse at 50% 55%,#f39a2a 0%,#d0501a 25%,#6a2412 55%,#1a1412 80%,#121212 100%)"></div>
    <div class="logo"><i></i>EMBERA CHARCOAL</div>
    <div class="cover-title">FUEL YOUR FIRE<br>WITH NAMIBIAN<br>PRECISION</div>
    <div class="bar-bottom"></div>
  </div>
</section>

<!-- Inside spread -->
<section class="spread spread--inside">
  <div class="panel panel--white">
    <svg class="photo" style="left:0;top:0" width="256" height="230" viewBox="0 0 256 230" role="img" aria-label="Photo of a chef cooking over a charcoal grill in a restaurant kitchen">
      <defs><linearGradient id="kitchen" x1="0" y1="0" x2="1" y2="1"><stop offset="0" stop-color="#6b4a2a"/><stop offset=".5" stop-color="#3a2a1e"/><stop offset="1" stop-color="#d87a2a"/></linearGradient></defs>
      <path d="M0 0H256V180Q200 240 128 222Q50 205 0 150Z" fill="#c4161c"/>
      <path d="M0 0H256V170Q200 232 128 215Q50 198 0 144Z" fill="url(#kitchen)"/>
    </svg>
    <div class="photo" role="img" aria-label="Kraft paper bag of restaurant charcoal" style="left:53px;top:113px;width:136px;height:172px;background:linear-gradient(180deg,#d4ab76,#b98e58);border-radius:3px"></div>
    <div class="product" style="top:306px">
      <div class="title"><span class="h-red">Product 1:</span><br>Embera Restaurant<br>Grade</div>
      <div class="sub">Engineered for Professional Kitchens</div>
      <p>Trusted by chefs who demand consistency, Embera Restaurant Grade charcoal is tailored for high-volume, high-performance cooking environments.</p>
      <ul class="bullets">
        <li>High, Stable Heat for grilling and searing</li>
        <li>Extended Burn Time for long service hours</li>
        <li>Minimal Ash Residue keeps kitchens cleaner</li>
        <li>Low Smoke Output ensures a pleasant cooking environment</li>
      </ul>
    </div>
    <div class="bar-bottom"></div>
  </div>

  <div class="panel panel--dark">
    <div class="science">
      <div class="title"><span class="h-red">The Science</span> Behind<br>Our Charcoal</div>
      <div class="kicker">WHY EMBERA OUTPERFORMS ORDINARY CHARCOAL</div>
    </div>
    <div class="feature" style="top:104px">
      <svg viewBox="0 0 34 34"><circle cx="17" cy="17" r="15" fill="#c4161c"/><text x="17" y="20.5" text-anchor="middle" font-family="Montserrat,sans-serif" font-weight="800" font-size="10" fill="#1d1d1d">CO2</text></svg>
      <div class="body"><h3>HIGHER CARBON CONTENT</h3><div class="rule"></div><p>Sed ut perspiciatis unde omnis iste natus error sit voluptatem accusantium doloremque laudantium, totam rem aperiam, eaque ipsa quae ab illo inventore veritatis et quasi architecto beatae vitae dicta sunt explicabo. Nemo enim ipsam voluptatem quia voluptas sit aspernatur aut odit aut fugit, sed quia consequuntur</p></div>
    </div>
    <div class="feature" style="top:189px">
      <svg viewBox="0 0 34 34"><circle cx="11" cy="12" r="6" fill="none" stroke="#c4161c" stroke-width="3"/><rect x="20" y="6" width="5" height="18" rx="2.5" fill="#c4161c"/><circle cx="22.5" cy="26" r="5" fill="#c4161c"/></svg>
      <div class="body"><h3>CONSISTENT HEAT OUTPUT</h3><div class="rule"></div><p>Sed ut perspiciatis unde omnis iste natus error sit voluptatem accusantium doloremque laudantium, totam rem aperiam, eaque ipsa quae ab illo inventore veritatis et quasi architecto beatae vitae dicta sunt explicabo. Nemo enim ipsam voluptatem quia voluptas sit aspernatur aut odit aut fugit, sed quia consequuntur</p></div>
    </div>
    <div class="feature" style="top:273px">
      <svg viewBox="0 0 34 34"><path d="M17 2C12 10 5 15 5 22a12 12 0 0 0 24 0C29 15 22 10 17 2z" fill="#c4161c"/><circle cx="17" cy="22" r="6" fill="none" stroke="#1d1d1d" stroke-width="2"/><path d="M17 19v3.5h3" stroke="#1d1d1d" stroke-width="1.6" fill="none"/></svg>
      <div class="body"><h3>LONGER BURN TIME</h3><div class="rule"></div><p>Sed ut perspiciatis unde omnis iste natus error sit voluptatem accusantium doloremque laudantium, totam rem aperiam, eaque ipsa quae ab illo inventore veritatis et quasi architecto beatae vitae dicta sunt explicabo. Nemo enim ipsam voluptatem quia voluptas sit aspernatur aut odit aut fugit, sed quia consequuntur</p></div>
    </div>
    <div class="feature" style="top:358px">
      <svg viewBox="0 0 34 34"><circle cx="12" cy="10" r="6" fill="#c4161c"/><circle cx="21" cy="9" r="6" fill="#c4161c"/><circle cx="17" cy="16" r="6" fill="#c4161c"/><circle cx="17" cy="26" r="2.5" fill="#c4161c"/><rect x="14" y="31" width="6" height="1.5" fill="#c4161c"/></svg>
      <div class="body"><h3>LOW SMOKE, LOW ASH</h3><div class="rule"></div><p>Sed ut perspiciatis unde omnis iste natus error sit voluptatem accusantium doloremque laudantium, totam rem aperiam, eaque ipsa quae ab illo inventore veritatis et quasi architecto beatae vitae dicta sunt explicabo. Nemo enim ipsam voluptatem quia voluptas sit aspernatur aut odit aut fugit, sed quia consequuntur</p></div>
    </div>
    <div class="feature" style="top:442px">
      <svg viewBox="0 0 34 34"><circle cx="17" cy="17" r="12" fill="none" stroke="#c4161c" stroke-width="6" stroke-dasharray="5 2.8"/><circle cx="17" cy="17" r="8" fill="#c4161c"/><path d="M13 20c0-5 4-8 8-8 0 5-3 8-8 8z" fill="#1d1d1d"/></svg>
      <div class="body"><h3>SUSTAINABLY PRODUCED</h3><div class="rule"></div><p>Sed ut perspiciatis unde omnis iste natus error sit voluptatem accusantium doloremque laudantium, totam rem aperiam, eaque ipsa quae ab illo inventore veritatis et quasi architecto beatae vitae dicta sunt explicabo. Nemo enim ipsam voluptatem quia voluptas sit aspernatur aut odit aut fugit, sed quia consequuntur</p></div>
    </div>
  </div>

  <div class="panel panel--white">
    <div class="bar-top"></div>
    <div class="product" style="top:28px;left:20px">
      <div class="title"><span class="h-red">Product 1:</span><br>Embera Barbecue<br>Grade</div>
      <div class="sub">Perfect for the Home Barbecue Enthusiast</div>
      <p style="text-align:justify">Embera Barbecue Grade makes every cookout a celebration. Designed to be easy to light and rich in aroma, it brings out the best in your barbecue flavors.</p>
      <ul class="bullets" style="margin-top:12px">
        <li>Enhanced Flavor &amp; Aroma that complements meat</li>
        <li>Quick Lighting &amp; Consistent Burn for stress-free grilling</li>
        <li>Reliable Heat for even cooking</li>
        <li>Premium Namibian Hardwood Base ensures natural quality</li>
      </ul>
    </div>
    <svg class="photo" style="left:0;bottom:0" width="256" height="230" viewBox="0 0 256 230" role="img" aria-label="Photo of charcoal burning with bright flames on a grill">
      <defs><radialGradient id="flames" cx=".5" cy=".7" r=".7"><stop offset="0" stop-color="#f5a02a"/><stop offset=".4" stop-color="#d8481a"/><stop offset=".8" stop-color="#4a1810"/><stop offset="1" stop-color="#1a1010"/></radialGradient></defs>
      <path d="M0 230V75Q128-30 256 75V230Z" fill="#c4161c"/>
      <path d="M0 230V82Q128-20 256 82V230Z" fill="url(#flames)"/>
    </svg>
    <div class="photo" role="img" aria-label="Kraft paper bag of barbecue charcoal" style="left:61px;top:283px;width:133px;height:172px;background:linear-gradient(180deg,#d4ab76,#b98e58);border-radius:3px"></div>
  </div>
</section>

</body>
</html>
```